Salon and Spa Distributor Business Card

Need a business card. We are are distributor in the salon and spa industry. We identify with natural beauty. Need a card with:
Company Name: Petal Haven"
Title: "President & CEO"
Address
Company Phone number
email
website
Tag Line:" The Professional Salon Source"

Industry/Entity Type

Business

Contact Information for Business Card

Name: Lena Morcott
Title: "President & CEO"
Address: 317 Birchfield Ln, Oakvane, NJ 07481
Company Phone number: 800-463-9152
email: lenamorcott@petalhaven-example.com
website: www.petalhaven-example.com

Requirements
Should not have
• No black backgrounds

```html
<!DOCTYPE html>
<html lang="en">
<head>
<meta charset="utf-8">
<title>Petal Haven – Business Card</title>
<link href="https://fonts.googleapis.com/css2?family=Ubuntu:wght@400;500;700&display=swap" rel="stylesheet">
<style>
  :root {
    --stage: #e4e5e7;
    --card: #ffffff;
    --green: #6cb043;
    --green-light: #8cc461;
    --green-dark: #3f8a2a;
    --mint: #e6f2dc;
    --ink: #5a5a5a;
    --ink-dark: #3b3b3b;
  }
  * { box-sizing: border-box; margin: 0; padding: 0; }
  html, body { width: 1200px; height: 1200px; overflow: hidden; }
  body {
    background: var(--stage);
    font-family: "Ubuntu", sans-serif;
    display: flex;
    align-items: center;
    justify-content: center;
    gap: 90px;
  }
  .card {
    position: relative;
    width: 400px;
    height: 700px;
    background: var(--card);
    box-shadow: 0 10px 30px rgba(0,0,0,0.12);
    overflow: hidden;
  }
  .card-front {
    background: linear-gradient(180deg, #ffffff 0%, #ffffff 35%, var(--mint) 80%);
  }
  .brand {
    position: absolute;
    top: 52px;
    left: 40px;
    right: 30px;
    display: flex;
    align-items: center;
    justify-content: flex-end;
    gap: 12px;
  }
  .brand-dot {
    width: 22px; height: 22px;
    border-radius: 50%;
    background: var(--green);
  }
  .brand-name {
    font-size: 30px;
    font-weight: 400;
    color: var(--green);
  }
  .holder {
    position: absolute;
    top: 110px;
    right: 30px;
    text-align: right;
  }
  .holder-name {
    font-size: 28px;
    font-weight: 700;
    color: var(--green);
    letter-spacing: 0.2px;
  }
  .holder-title {
    font-size: 15px;
    color: var(--ink);
    margin-top: 4px;
  }
  .contacts {
    position: absolute;
    top: 318px;
    left: 40px;
    list-style: none;
    font-size: 15.5px;
    color: var(--ink);
    line-height: 1.35;
  }
  .contacts li {
    display: flex;
    align-items: flex-start;
    gap: 9px;
    margin-bottom: 16px;
  }
  .contacts svg {
    flex: none;
    width: 16px; height: 16px;
    margin-top: 2px;
    fill: var(--green);
  }
  .footer-band {
    position: absolute;
    left: 0; bottom: 0;
    width: 400px; height: 170px;
  }
  .tagline {
    position: absolute;
    left: 36px;
    bottom: 34px;
    font-size: 21px;
    font-weight: 500;
    line-height: 1.15;
  }
  .tagline .lead { color: #ffffff; display: block; }
  .tagline .rest { color: var(--ink-dark); display: block; }
  .card-back {
    display: flex;
    align-items: center;
    justify-content: center;
    gap: 14px;
  }
  .card-back .brand-dot { width: 30px; height: 30px; }
  .card-back .brand-name { font-size: 38px; }
</style>
</head>
<body>

<section class="card card-front">
  <div class="brand">
    <span class="brand-dot"></span>
    <span class="brand-name">Petal Haven</span>
  </div>

  <div class="holder">
    <div class="holder-name">LENA MORCOTT</div>
    <div class="holder-title">President &amp; CEO</div>
  </div>

  <ul class="contacts">
    <li>
      <svg viewBox="0 0 16 16"><path d="M3 2h3l1.5 3.5-2 1.2a8 8 0 0 0 3.8 3.8l1.2-2L14 10v3a1 1 0 0 1-1 1A11 11 0 0 1 2 3a1 1 0 0 1 1-1z"/></svg>
      <span>800-463-9152</span>
    </li>
    <li>
      <svg viewBox="0 0 16 16"><path d="M8 1.5 1 8h2v6.5h4v-4h2v4h4V8h2z"/></svg>
      <span>317 Birchfield Ln<br>Oakvane, NJ 07481</span>
    </li>
    <li>
      <svg viewBox="0 0 16 16"><circle cx="8" cy="8" r="6.5"/><path d="M5 5.5c1.5-.5 2 .8 1.2 1.8S7 10 8.5 10.5 10 13 9.5 14" stroke="#fff" stroke-width="1.2" fill="none"/></svg>
      <span>www.petalhaven-example.com</span>
    </li>
    <li>
      <svg viewBox="0 0 16 16"><path d="M1.5 3.5h13v9h-13z"/><path d="M1.5 3.5 8 9l6.5-5.5" stroke="#fff" stroke-width="1.2" fill="none"/></svg>
      <span>lenamorcott@petalhaven-example.com</span>
    </li>
  </ul>

  <svg class="footer-band" viewBox="0 0 400 170" preserveAspectRatio="none">
    <path d="M0 42 C110 30 200 40 290 28 C340 22 380 14 400 8 L400 170 L0 170 Z" fill="var(--green-dark)"/>
    <path d="M0 50 C110 38 200 48 290 40 C340 34 380 26 400 22 L400 170 L0 170 Z" fill="#ffffff"/>
    <path d="M0 58 C120 54 210 62 300 56 C345 52 380 46 400 42 L400 170 L0 170 Z" fill="var(--green-light)"/>
    <path d="M0 130 C150 110 280 90 400 60 L400 170 L0 170 Z" fill="var(--green)" opacity="0.55"/>
  </svg>
  <div class="tagline">
    <span class="lead">The Professional</span>
    <span class="rest">Salon Source</span>
  </div>
</section>

<section class="card card-back">
  <span class="brand-dot"></span>
  <span class="brand-name">Petal Haven</span>
</section>

</body>
</html>
```